Chiropractic Business /Appointment Card Design

We are a wellness based well est. chiropractic under new ownership. I have logo with old name looking to change up with new name, maybe design. I like three people logo but I don't like colors or name layout. Looking for ideas, thinking Maroon(more red then brown) and/ or metallic Gold, silver, bronze. I would like to incorporate design and layouts on business cards for other employees, letterhead, envelopes, magnets, etc.

Target Market(s)

0-65 wellness minded

Industry/Entity Type

Business

Contact Information for Business Card

Brackwell Lane Family Chiropractic
Dr. Marlon Fenwick
Chiropractor
47 Tamsin R. Drive
Harlow Springs, NY 13642
607-555-0184
www.quillmeadvital.example
Office Hours:
Monday 9-12, 2:30-5
Tuesday 2:30-6
Wednesday 9-12, 2:30-5
Thursday 9-12, 2:30-6
Date Time
______ _______
______ _______
______ ______
______ ______
______ ______

Requirements
Must have
• three people (attached)

```html
<!DOCTYPE html>
<html lang="en">
<head>
<meta charset="utf-8">
<title>Brackwell Lane Family Chiropractic – Business &amp; Appointment Card</title>
<link rel="stylesheet" href="https://fonts.googleapis.com/css2?family=Arimo:wght@400;700&display=swap">
<style>
  :root {
    --maroon: #98191d;
    --bronze: #a57c52;
    --sky: #1aa7e0;
    --ink: #1d1d1d;
    --paper: #ffffff;
    --backdrop: #d9dadc;
    --rule: #444;
  }
  * { box-sizing: border-box; margin: 0; padding: 0; }
  html, body { width: 1200px; height: 900px; overflow: hidden; }
  body {
    background: var(--backdrop);
    font-family: "Arimo", Arial, sans-serif;
    color: var(--ink);
    display: flex;
    flex-direction: column;
    align-items: center;
    justify-content: center;
    gap: 56px;
  }
  .card {
    position: relative;
    width: 630px;
    height: 360px;
    background: var(--paper);
    box-shadow: 0 6px 18px rgba(0,0,0,.18);
    overflow: hidden;
  }

  /* Business card (front) */
  .brand {
    position: absolute;
    left: 48px;
    top: 50px;
    display: flex;
    align-items: center;
    gap: 16px;
  }
  .brand__dot {
    width: 58px; height: 58px;
    border-radius: 50%;
    background: var(--maroon);
    flex: none;
  }
  .brand__name {
    font-size: 27px;
    line-height: 1.1;
    color: var(--maroon);
    font-weight: 400;
  }
  .doctor {
    position: absolute;
    left: 48px;
    top: 196px;
    font-size: 21px;
    color: var(--maroon);
    white-space: nowrap;
  }
  .doctor__title { font-size: 14px; color: var(--ink); }
  .address {
    position: absolute;
    left: 48px;
    top: 240px;
    font-size: 15px;
    line-height: 1.5;
  }
  .contact {
    position: absolute;
    left: 362px;
    top: 180px;
    font-size: 15px;
    line-height: 1.55;
    white-space: nowrap;
  }
  .contact__label { font-size: 9px; text-transform: uppercase; letter-spacing: .03em; margin-right: 4px; }
  .contact__label--phone { color: var(--bronze); }
  .contact__label--web { color: var(--sky); }
  .colour-band {
    position: absolute;
    left: 0; right: 0; bottom: 0;
    height: 16px;
    display: flex;
  }
  .colour-band span:nth-child(1) { flex: 0 0 38%; background: var(--maroon); }
  .colour-band span:nth-child(2) { flex: 0 0 37%; background: var(--bronze); }
  .colour-band span:nth-child(3) { flex: 1; background: var(--sky); }

  /* Appointment card (back) */
  .appt__header {
    position: absolute;
    left: 0; right: 0; top: 0;
    height: 196px;
    background: var(--maroon);
    display: flex;
    align-items: center;
    justify-content: center;
    border-bottom: 4px solid var(--bronze);
  }
  .appt__stripe {
    position: absolute;
    left: 0; right: 0; top: 200px;
    height: 7px;
    background: var(--sky);
  }
  .appt__brand {
    display: flex;
    align-items: center;
    gap: 14px;
  }
  .appt__brand .brand__dot { background: var(--paper); width: 50px; height: 50px; }
  .appt__brand .brand__name { color: var(--paper); font-size: 28px; }
  .hours {
    position: absolute;
    left: 44px;
    top: 232px;
    font-size: 14px;
    line-height: 1.5;
  }
  .hours__day--mon, .hours__day--thu { color: var(--maroon); }
  .hours__day--tue { color: var(--bronze); }
  .hours__day--wed { color: var(--sky); }
  .appointment {
    position: absolute;
    left: 44px;
    top: 300px;
    font-size: 14px;
    display: flex;
    align-items: flex-end;
    gap: 6px;
  }
  .appointment__line {
    display: inline-block;
    width: 150px;
    border-bottom: 1px solid var(--rule);
    height: 14px;
    margin-right: 18px;
  }
</style>
</head>
<body>

  <section class="card card--business" aria-label="Business card">
    <div class="brand">
      <div class="brand__dot"></div>
      <div class="brand__name">Brackwell Lane<br>Family Chiropractic</div>
    </div>
    <p class="doctor">Dr. Marlon Fenwick, <span class="doctor__title">Chiropractor</span></p>
    <p class="address">47 Tamsin R. Drive<br>Harlow Springs, NY 13642</p>
    <p class="contact">
      <span class="contact__label contact__label--phone">Phone:</span>607-555-0184<br>
      <span class="contact__label contact__label--web">Website:</span>www.quillmeadvital.example
    </p>
    <div class="colour-band"><span></span><span></span><span></span></div>
  </section>

  <section class="card card--appointment" aria-label="Appointment card">
    <div class="appt__header">
      <div class="appt__brand">
        <div class="brand__dot"></div>
        <div class="brand__name">Brackwell Lane<br>Family Chiropractic</div>
      </div>
    </div>
    <div class="appt__stripe"></div>
    <p class="hours">
      Office Hours:<br>
      <span class="hours__day--mon">Monday</span> 9-12, 2:30-5
      <span class="hours__day--tue">Tuesday</span> 2:30-6
      <span class="hours__day--wed">Wednesday</span> 9-12, 2:30-5
      <span class="hours__day--thu">Thursday</span> 9-12, 2:30-6
    </p>
    <p class="appointment">
      Appointment:&nbsp; Date: <span class="appointment__line"></span>
      Time: <span class="appointment__line"></span>
    </p>
  </section>

</body>
</html>
```